Professional Modern Website Design

We are a premium IT services provider to the financial industry based in London. Our company is called Veltra our current holding page is www.veltra-example.co.uk. We require a new website to match our new corporate identity. This project is for the design phase only. Development will be handled in-house. I have attached examples of wire frames we have developed (although open to suggestions for improvement) Our brand document that should demonstrate current brand, inc how we communicate to potential clients and finally mostly completed web-content.
We are looking for designers that can create something that sets us apart from our competitors.
Target Market(s)
IT Decision makers in Finance companies such as; hedge funds, private investment banks etc
Industry/Entity Type
Financial
Number of Pages Required
5+ page
Requirements
Must have
- hexagon elements in the design, unique design.
Nice to have
- Blog and social media feeds
Should not have
- Should not resemble a downloaded template

```html
<!DOCTYPE html>
<html lang="en">
<head>
<meta charset="utf-8">
<title>Veltra – Data Centre &amp; Infrastructure</title>
<link href="https://fonts.googleapis.com/css2?family=Source+Sans+3:wght@400;600;700&display=swap" rel="stylesheet">
<style>
  :root {
    --orange: #e35a24;
    --orange-bright: #f26a21;
    --orange-soft: rgba(226, 96, 40, 0.85);
    --rust: #b6380f;
    --ink: #1b1b1b;
    --body-ink: #3b2a20;
    --white: #ffffff;
    --footer-bg: #e2d9d5;
    --footer-ink: #6a6462;
    --logo-grey: #7d7d7d;
  }
  * { box-sizing: border-box; margin: 0; padding: 0; }
  html, body { width: 1144px; height: 1200px; overflow: hidden; background: var(--white); }
  body { font-family: "Source Sans 3", "Source Sans Pro", sans-serif; color: var(--ink); }
  .page { position: relative; width: 1144px; height: 1200px; }

  .top-bar { position: absolute; left: 0; top: 0; width: 1144px; height: 63px; background: var(--orange); z-index: 3; }
  .top-nav a {
    position: absolute; top: 22px; color: var(--white); text-decoration: none;
    font-weight: 600; font-size: 16.5px; letter-spacing: .2px;
  }
  .brand-tab { position: absolute; left: 432px; top: 0; width: 190px; height: 118px; z-index: 4; }
  .brand-tab svg { position: absolute; inset: 0; }
  .brand-name {
    position: absolute; left: 0; right: 0; top: 44px; text-align: center;
    font-weight: 700; font-size: 24px; letter-spacing: 3px; color: var(--orange);
  }
  .brand-name .mark { display: inline-block; width: 12px; height: 12px; background: var(--orange); margin-right: 8px; vertical-align: 2px; }

  .hero {
    position: absolute; left: 0; top: 63px; width: 1144px; height: 564px;
    background:
      radial-gradient(ellipse at 25% 30%, rgba(140,170,90,.55), transparent 45%),
      radial-gradient(ellipse at 60% 25%, rgba(90,140,190,.45), transparent 45%),
      radial-gradient(ellipse at 40% 70%, rgba(20,20,20,.55), transparent 55%),
      linear-gradient(180deg, #4a4c4e 0%, #5b5d5f 70%, #9a9896 100%);
  }
  .service-card { position: absolute; left: 616px; top: 194px; width: 468px; }
  .service-card__title {
    position: relative; height: 58px; background: var(--white); border-radius: 3px 3px 0 0;
    padding: 16px 0 0 41px; font-weight: 700; font-size: 21px; color: var(--rust); letter-spacing: .2px;
  }
  .service-card__title::after {
    content: ""; position: absolute; left: 44px; bottom: -10px;
    border-left: 10px solid transparent; border-right: 10px solid transparent; border-top: 10px solid var(--white);
  }
  .service-card__panel { background: var(--orange-soft); height: 314px; padding: 24px 22px; }
  .service-card__body {
    background: rgba(255,255,255,.97); border-radius: 4px; height: 269px; padding: 24px 22px;
    font-weight: 600; font-size: 11.5px; line-height: 20px; text-transform: uppercase; color: var(--ink);
    letter-spacing: .25px;
  }
  .service-card__body p + p { margin-top: 9px; }

  .steps { position: absolute; left: 0; top: 697px; width: 1144px; }
  .step { position: absolute; top: 0; width: 330px; text-align: center; }
  .step__frame { position: relative; width: 184px; height: 184px; margin: 0 auto; }
  .step__frame svg { display: block; }
  .step__title { margin-top: 11px; font-weight: 600; font-size: 15px; letter-spacing: .2px; color: var(--ink); }
  .step__pointer { display: block; margin: 5px auto 0; }
  .step__text { margin-top: 14px; font-weight: 600; font-size: 13px; line-height: 20px; color: var(--body-ink); }

  .site-footer { position: absolute; left: 0; top: 1112px; width: 1144px; height: 88px; background: var(--footer-bg); }
  .footer-brand {
    position: absolute; left: 59px; top: 32px; font-weight: 700; font-size: 22px; letter-spacing: 1px; color: var(--logo-grey);
  }
  .footer-nav a {
    position: absolute; top: 38px; text-decoration: none; font-weight: 600; font-size: 13px;
    color: var(--footer-ink); letter-spacing: .2px;
  }
  .footer-nav a.is-active { color: var(--orange-bright); }
</style>
</head>
<body>
<div class="page">

  <header class="top-bar">
    <nav class="top-nav">
      <a href="#" style="left:204px">ABOUT</a>
      <a href="#" style="left:307px">SERVICES</a>
      <a href="#" style="left:657px">PARTNERS</a>
      <a href="#" style="left:781px">CLIENTS</a>
      <a href="#" style="left:896px">CONTACT</a>
    </nav>
  </header>

  <div class="brand-tab">
    <svg width="190" height="118" viewBox="0 0 190 118">
      <polygon points="4,-2 186,-2 186,86 152,114 38,114 4,86" fill="#ffffff" stroke="#f26a21" stroke-width="5"/>
    </svg>
    <div class="brand-name"><span class="mark"></span>VELTRA</div>
  </div>

  <section class="hero" role="img" aria-label="Photo: four business people standing before a wall covered in colourful chalk diagrams">
    <article class="service-card">
      <h1 class="service-card__title">DATA CENTRE &amp; INFRASTUCTURE</h1>
      <div class="service-card__panel">
        <div class="service-card__body">
          <p>We set our standards high, aiming to become an industry leader within the finance sector for delivering secure, scalable and always available infrastructure.</p>
          <p>We consult with you on data centre best practices. We will consider the data centre location, provider and design, including build and configuration to make sure it aligns with your expectations.</p>
          <p>We merge the best products with top-class maintenance services to ensure our integration meets your objectives.</p>
        </div>
      </div>
    </article>
  </section>

  <section class="steps">
    <div class="step" style="left:53px">
      <div class="step__frame">
        <svg width="184" height="184" viewBox="0 0 184 184">
          <defs><linearGradient id="photoTone" x1="0" y1="0" x2="1" y2="1"><stop offset="0" stop-color="#c9d3dc"/><stop offset=".55" stop-color="#a9b4bf"/><stop offset="1" stop-color="#6d747b"/></linearGradient></defs>
          <polygon points="52,3 132,3 181,52 181,128 132,172 52,172 3,128 3,52" fill="url(#photoTone)" stroke="#f26a21" stroke-width="5" role="img" aria-label="Photo: hands using a tablet showing charts"/>
          <polygon points="80,172 104,172 92,184" fill="#f26a21"/>
        </svg>
      </div>
      <h2 class="step__title">ANALYSIS &amp; ASSESSMENT</h2>
      <svg class="step__pointer" width="24" height="10" viewBox="0 0 24 10"><polygon points="0,0 24,0 12,10" fill="#f26a21"/></svg>
      <p class="step__text">We will analyse your current infrastructure and assess what you need to help your business grow. We can offer advice on both on and off-premise solutions to meet compliance and your enterprise’s objectives.</p>
    </div>

    <div class="step" style="left:401px">
      <div class="step__frame">
        <svg width="184" height="184" viewBox="0 0 184 184">
          <polygon points="52,3 132,3 181,52 181,128 132,172 52,172 3,128 3,52" fill="url(#photoTone)" stroke="#f26a21" stroke-width="5" role="img" aria-label="Photo: hands using a tablet showing charts"/>
          <polygon points="80,172 104,172 92,184" fill="#f26a21"/>
        </svg>
      </div>
      <h2 class="step__title">IMPLEMENTATION</h2>
      <svg class="step__pointer" width="24" height="10" viewBox="0 0 24 10"><polygon points="0,0 24,0 12,10" fill="#f26a21"/></svg>
      <p class="step__text">We will implement the best solutions for you and ensure everything you need is set up without a gap in service. If you need to migrate applications or services, we will ensure it runs smoothly and all risks are addressed ahead of time.</p>
    </div>

    <div class="step" style="left:765px">
      <div class="step__frame">
        <svg width="184" height="184" viewBox="0 0 184 184">
          <polygon points="52,3 132,3 181,52 181,128 132,172 52,172 3,128 3,52" fill="url(#photoTone)" stroke="#f26a21" stroke-width="5" role="img" aria-label="Photo: hands using a tablet showing charts"/>
          <polygon points="80,172 104,172 92,184" fill="#f26a21"/>
        </svg>
      </div>
      <h2 class="step__title">ADAPT AND GROW</h2>
      <svg class="step__pointer" width="24" height="10" viewBox="0 0 24 10"><polygon points="0,0 24,0 12,10" fill="#f26a21"/></svg>
      <p class="step__text">Although everything we do is scalable, we under­stand businesses change. We will continually assess your needs and adapt as you do. Because we are an integrator, we can watch from the sidelines to ensure opportunities are never missed.</p>
    </div>
  </section>

  <footer class="site-footer">
    <div class="footer-brand">Veltra</div>
    <nav class="footer-nav">
      <a href="#" class="is-active" style="left:676px">ABOUT</a>
      <a href="#" style="left:757px">SERVICES</a>
      <a href="#" style="left:846px">PARTNERS</a>
      <a href="#" style="left:945px">CLIENTS</a>
      <a href="#" style="left:1029px">CONTACT</a>
    </nav>
  </footer>

</div>
</body>
</html>
```